Letterhead and Business card for Construction company

We need a letterhead and business card with our new company logo. We are based in NY. We develop and build properties.

The design should incorporate some unique feature from the logo (shape, font...). it should look like an extension from it.

Design should be clean and elegant, professional, not too busy.

The letterhead should include:
Logo (attached)
Address
Phone
Email

Please find the attached logo images and AI file.

Target Market(s)

Construction industry professionals

Industry/Entity Type

Construction, Development

Font styles to use
Sans Serif

Colors

Designer to choose colors to be used in the design.

Requirements
Must have
• Design should incorporate logo elements, additional assets are welcome. I'd like to see some other shapes / images invorporated too.

```html
<!DOCTYPE html>
<html lang="en">
<head>
<meta charset="utf-8">
<title>KRB Contracting – Business Card</title>
<link rel="stylesheet" href="https://fonts.googleapis.com/css2?family=Montserrat:wght@400;700&display=swap">
<style>
  :root {
    --page-bg: #2a2b30;
    --card-dark: #1c1d21;
    --card-dark-edge: #27282d;
    --card-light: #e9e9ef;
    --accent: #e0953d;
    --ink-grey: #4b4c54;
    --text-light: #d6d7de;
    --text-muted: #b4b5bd;
  }
  * { box-sizing: border-box; margin: 0; padding: 0; }
  html, body { width: 1200px; height: 800px; overflow: hidden; }
  body {
    background: var(--page-bg);
    font-family: "Montserrat", Arial, sans-serif;
    position: relative;
  }
  .card {
    position: absolute;
    top: 137px;
    width: 300px;
    height: 526px;
    border-radius: 16px;
    overflow: hidden;
  }
  .card--front { left: 255px; }
  .card--back {
    left: 645px;
    background: linear-gradient(160deg, var(--card-dark-edge), var(--card-dark));
  }
  .card__bg { position: absolute; inset: 0; width: 100%; height: 100%; }

  .wordmark {
    position: absolute;
    left: 0; right: 0;
    text-align: center;
    font-weight: 700;
    text-transform: uppercase;
    line-height: 1.05;
  }
  .wordmark__name { display: block; font-size: 48px; letter-spacing: 2px; }
  .wordmark__sub { display: block; font-size: 17px; letter-spacing: 3px; }
  .card--front .wordmark { top: 92px; color: var(--ink-grey); }
  .card--back .wordmark { top: 205px; color: var(--text-light); }

  .contact {
    position: absolute;
    left: 44px;
    top: 348px;
    color: var(--text-light);
  }
  .contact__company { font-size: 19px; font-weight: 400; letter-spacing: .3px; line-height: 1.2; }
  .contact__company strong { font-weight: 700; }
  .contact__role { font-size: 14px; color: var(--text-muted); letter-spacing: .5px; margin-bottom: 16px; }
  .contact__list { list-style: none; }
  .contact__item {
    display: flex; align-items: center; gap: 10px;
    font-size: 15.5px; color: var(--text-light);
    margin-bottom: 8px;
  }
  .contact__icon { width: 15px; height: 15px; fill: var(--text-light); flex: none; }
</style>
</head>
<body>

  <section class="card card--front" aria-label="Business card front">
    <svg class="card__bg" viewBox="0 0 300 526" preserveAspectRatio="none" aria-hidden="true">
      <rect width="300" height="526" fill="#1f2024"/>
      <polygon points="0,0 300,0 300,222 0,318" fill="#e9e9ef"/>
      <polygon points="0,318 300,222 300,232 0,336" fill="#e0953d"/>
    </svg>
    <div class="wordmark">
      <span class="wordmark__name">KRB</span>
      <span class="wordmark__sub">Contracting</span>
    </div>
    <div class="contact">
      <p class="contact__company"><strong>KRB</strong> CONTRACTING</p>
      <p class="contact__role">CONSTRUCTION</p>
      <ul class="contact__list">
        <li class="contact__item">
          <svg class="contact__icon" viewBox="0 0 24 24"><path d="M6.6 10.8a15.1 15.1 0 0 0 6.6 6.6l2.2-2.2a1 1 0 0 1 1-.25 11.4 11.4 0 0 0 3.6.57 1 1 0 0 1 1 1V20a1 1 0 0 1-1 1A17 17 0 0 1 3 4a1 1 0 0 1 1-1h3.5a1 1 0 0 1 1 1c0 1.25.2 2.45.57 3.57a1 1 0 0 1-.25 1z"/></svg>
          555 014 2290
        </li>
        <li class="contact__item">
          <svg class="contact__icon" viewBox="0 0 24 24"><path d="M2 5h20v14H2z" fill="none" stroke="#d6d7de" stroke-width="2"/><path d="M2 5l10 8 10-8" fill="none" stroke="#d6d7de" stroke-width="2"/></svg>
          yourmail@email.com
        </li>
        <li class="contact__item">
          <svg class="contact__icon" viewBox="0 0 24 24"><path d="M12 2a7 7 0 0 0-7 7c0 5.2 7 13 7 13s7-7.8 7-13a7 7 0 0 0-7-7zm0 9.5A2.5 2.5 0 1 1 12 6.5a2.5 2.5 0 0 1 0 5z"/></svg>
          youraddress
        </li>
      </ul>
    </div>
  </section>

  <section class="card card--back" aria-label="Business card back">
    <div class="wordmark">
      <span class="wordmark__name">KRB</span>
      <span class="wordmark__sub">Contracting</span>
    </div>
  </section>

</body>
</html>
```